Geschäftspapiere für Hundebetreuung
Zielgruppe
Mein Unternehmen richtet sich an Hundehalter, die freudig mit ihrem Hund arbeiten oder trainieren wollen oder eine positiv arbeitende Hundebetreuung oder Gassi-Gänger suchen. Hierbei liegt der Fokus auf Emotionen des Hundes, Emotionen des Hundehalters, Körpersprache und kleinschrittiges Training. Gemeinsames freudiges Training schafft Vertrauen und Bindung und ermöglicht Hund und Halter Freiraum. Ziel des Angebotes ist es, dass Hundehalter Verständnis für die Emotionen und Interessen des Hundes zu entwickeln und das für sich zu nutzen lernen, dem Hund das geben, was er in der jeweiligen Situation braucht und das ganze auf wissenschaftlich fundierter Basis.
Aufgabenstellung
Das Logo muss enthalten sein, ansonsten sind der Kreativität keine Grenzen gesetzt :)
Es sollte nur von Rechnung, über Angebot für alles nutzbar sein.
Das Unternehmen ist ein Einzelunternehmen, sprich der Firmenname ist mein eigener Name 'Sabine Krollmann' und Pfotenfreunde nur Website und Marke.

```html
<!DOCTYPE html>
<html lang="de">
<head>
<meta charset="utf-8">
<title>Pfotenfreunde – Briefbogen</title>
<link href="https://fonts.googleapis.com/css2?family=Poppins:ital,wght@0,300;0,400;0,600;1,300;1,400&display=swap" rel="stylesheet">
<style>
:root{
  --bg:#dedede;
  --paper:#ffffff;
  --green:#8cb92a;
  --slate:#3c4f57;
  --text:#3a4a52;
  --white:#ffffff;
}
*{box-sizing:border-box;margin:0;padding:0}
html,body{width:1200px;height:898px;overflow:hidden;background:var(--bg)}
body{font-family:"Poppins",sans-serif;color:var(--text);display:flex;align-items:center;justify-content:center}
.letter{position:relative;width:608px;height:860px;background:var(--paper);box-shadow:0 6px 24px rgba(0,0,0,.12);overflow:hidden}
.web-top{position:absolute;left:58px;top:58px;font-size:9.5px;font-weight:600;color:var(--slate)}
.brand{position:absolute;right:58px;top:40px;display:flex;align-items:center;gap:8px;font-size:22px;font-weight:600;color:var(--green)}
.brand-dot{width:14px;height:14px;border-radius:50%;background:var(--slate)}
.sender-line{position:absolute;left:58px;top:150px;font-size:6.2px;color:var(--green)}
.sender-line b{font-weight:600}
.recipient{position:absolute;left:58px;top:166px;font-size:9px;line-height:1.45;color:var(--slate)}
.recipient b{font-weight:600}
.date{position:absolute;right:58px;top:226px;font-size:8.5px;color:var(--slate)}
.fold{position:absolute;left:0;width:16px;height:1px;background:#c9c9c9}
.content{position:absolute;left:84px;right:58px;top:290px;font-size:8.6px;line-height:1.55}
.subject{font-size:11px;font-weight:600;color:var(--slate);margin-bottom:12px}
.content p{font-style:italic;font-weight:300;margin-bottom:12px}
.closing{font-style:italic;font-weight:300;margin-top:16px}
.footer{position:absolute;left:0;bottom:0;width:608px;height:220px}
.footer svg{position:absolute;inset:0}
.foot{position:absolute;color:var(--white);font-size:6.4px;line-height:1.5}
.foot b{font-weight:600}
.foot-name{left:62px;bottom:36px;font-size:9px;font-weight:600;color:var(--slate)}
.foot-addr{left:186px;bottom:30px}
.foot-contact{left:300px;bottom:48px}
.foot-contact span{display:flex;align-items:center;gap:4px}
.foot-contact svg{width:6px;height:6px;fill:var(--white)}
.foot-bank{left:448px;bottom:62px}
.foot-bank .label{color:var(--slate);font-weight:600}
.foot-bank td{padding-right:10px}
</style>
</head>
<body>
<main class="letter">
  <div class="web-top">www.pfotenfreunde.de</div>
  <div class="brand"><span class="brand-dot"></span>Pfotenfreunde</div>

  <div class="sender-line"><b>Pfotenfreunde GmbH</b> &nbsp;|&nbsp; Musterstraße 1 &nbsp;|&nbsp; 12345 Musterstadt</div>
  <address class="recipient" style="font-style:normal">
    <b>Musterfirma GmbH</b><br>Max Mustermann<br>Musterstraße 123<br>12345 Musterstadt
  </address>
  <div class="date">Musterstadt, 01.01.2022</div>

  <span class="fold" style="top:298px"></span>
  <span class="fold" style="top:425px"></span>

  <section class="content">
    <h1 class="subject">Betreff: Endam, omni dolor sam asperro que eos es</h1>
    <p>Uptassi quo volupta dit aliberis dolutas pelestrum sendi remquam repellent as autemodis etu­rit faciae illorrorest, omnimilit, qui ut endiscillam quid que sandero eiunt eror rest quam, tem­porunt officip sandam imi, sit acepudandis cor si cus, cum adios nonsedipsa consequ aesedit rem. Minus, inis am nos nossus vendaer uptiis mi, quiae con possi natis etur, simagna tionsed ullo venditia id ut auda isqui occus.</p>
    <p>Porest ma dolupta et accusdamusam sunt omnimil laborestia con commolum fugiaerio et iunt labor sequi velite et desciis sero modis nullandes del molliquo iliquis et eaquaspere sitiis es ele­nis dolendant exceperes es elenis dolendant exceperes es everest ibeatentia voloris ad millate il inctur? eatentia voloris ad millate il inctur? Qui vent venti ilibus.</p>
    <p>Excessi vel maximpo rporepe poreperum qui omniste eatenda quo es et omniaepudam, qui debissinci ullabor eptatempor modiorrum quos sus dolum ad quos et quias alissi debis nullore strunt porerum, sit vole.</p>
    <div class="closing">Herzlichst,<br>Erika Mustermann</div>
  </section>

  <footer class="footer">
    <svg viewBox="0 0 608 220" preserveAspectRatio="none" aria-hidden="true">
      <path d="M0 92 C60 70 110 80 170 58 C280 20 420 0 608 0 L608 220 L0 220 Z" fill="var(--green)"/>
      <path d="M0 72 C20 90 60 94 110 88 C70 96 30 98 4 92 Z" fill="var(--slate)"/>
    </svg>
    <div class="foot foot-name">Pfotenfreunde GmbH</div>
    <div class="foot foot-addr">Musterstraße 1<br>12345 Musterstadt<br><b>Geschäftsführung:</b><br>Erika Mustermann</div>
    <div class="foot foot-contact">
      <span><svg viewBox="0 0 10 10"><path d="M2 0l2 2-1 2c1 1 2 2 3 3l2-1 2 2-2 2C4 10 0 6 0 2z"/></svg>+49 (0)1234 – 123 456 78</span>
      <span><svg viewBox="0 0 10 10"><rect x="2" y="0" width="6" height="10" rx="1"/></svg>+49 (0)1234 – 123 456 78</span>
      <span><svg viewBox="0 0 10 10"><path d="M0 2h10v6H0z"/></svg>kontakt@pfotenfreunde.de</span>
      <span><b>www.pfotenfreunde.de</b></span>
    </div>
    <div class="foot foot-bank">
      <div class="label">Bankverbindung</div>
      <b>Musterbank AG</b>
      <table><tr><td><b>IBAN:</b></td><td>DE12 1234 1234 1234 1234 00</td></tr>
      <tr><td><b>BIC:</b></td><td>ABCDEFGHJK</td></tr></table>
    </div>
  </footer>
</main>
</body>
</html>
```